Einladungskarten-Design zum 30. im Velvet Orchard Style
Zielgruppe
Ich feiere mit einem Freund gemeinsam 30. Geburtstag in 2020 und wir möchten gerne ein ausgefallenes und dem Anlass entsprechendes Design für ein Save the Date sowie im Nachgang auch eine volle Einladung designen lassen.
Aufgabenstellung
Das Design der Save the Date Karte soll bitte analog zu den angehängten Beispielen der Veranstaltung 'Velvet Orchard' im TR-83 auf Ibiza aufgesetzt werden. Die Veranstaltung findet auf Ibiza statt und wird das Motto 'Ibiza Jungle' tragen. Es handelt sich um eine schicke, jedoch exzentrische und auch verrückte Abendveranstaltung bei der sich die Gäste ausgefallenen und getreu dem Motto anziehen werden. Dieses Motto soll in der Einladung bereits berücksichtigt werden. Das Format sollte A5 Hoch- oder Querformat sein. Es handelt sich um eine private Veranstaltung bei der die Karten ausschließlich an geladene Gäste verschickt werden, es findet also keine kommerzielle Nutzung, Werbung oder sonstige Veröffentlichung der Karte statt.

```html
<!DOCTYPE html>
<html lang="en">
<head>
<meta charset="utf-8">
<title>Save the Date – Dirty Thirty Ibiza</title>
<link rel="stylesheet" href="https://fonts.googleapis.com/css2?family=Permanent+Marker&display=block">
<style>
  :root {
    --paper: #ffffff;
    --frame: #c9c9c9;
    --ink: #111111;
    --text: #ffffff;
    --violet: #8a4fb0;
    --purple: #7a2fc0;
    --lilac: #c58adf;
    --indigo: #3420b0;
    --royal: #2f62e6;
    --sky: #7fd6ea;
    --teal: #36d8b8;
    --magenta: #b05ba8;
    --lime: #d8f53a;
    --parrot: #8fc92a;
    --scale: #1f2a2a;
    --pale: #d9dde6;
  }
  * { box-sizing: border-box; margin: 0; padding: 0; }
  html, body { width: 934px; height: 1200px; overflow: hidden; background: var(--paper); }
  .canvas {
    position: relative; width: 934px; height: 1200px;
    background: var(--paper); border: 1px solid var(--frame);
  }
  .card {
    position: absolute; left: 115px; top: 101px; width: 703px; height: 997px;
    overflow: hidden; box-shadow: 0 2px 8px rgba(0,0,0,.35);
    background: var(--indigo);
    font-family: "Permanent Marker", "Marker Felt", "Comic Sans MS", cursive;
    color: var(--text); text-transform: uppercase;
  }
  .jungle-collage { position: absolute; inset: 0; width: 703px; height: 997px; }
  .line {
    position: absolute; left: 0; width: 100%; text-align: center;
    white-space: nowrap; transform: rotate(-5deg);
    -webkit-text-stroke: 5px var(--ink); paint-order: stroke fill;
    line-height: 1; font-weight: 400;
  }
  .title {
    top: 76px; font-size: 86px; transform: rotate(-9deg);
    -webkit-text-stroke: 12px var(--violet); text-transform: none;
  }
  .place { top: 163px; left: 172px; font-size: 44px; -webkit-text-stroke: 8px var(--violet); transform: rotate(-7deg); }
  .dates { top: 237px; font-size: 27px; }
  .hosts { top: 288px; font-size: 42px; }
  .hosts small { font-size: 24px; }
  .present { top: 342px; font-size: 17px; letter-spacing: 1px; }
  .event { top: 371px; font-size: 48px; }
  .label { font-size: 19px; }
  .item { font-size: 25px; }
  .detail { font-size: 19px; }
  .theme { font-size: 27px; }
  .rsvp {
    top: 938px; left: 14px; font-size: 16px; color: var(--lilac);
    -webkit-text-stroke: 3px var(--paper); transform: rotate(-7deg);
  }
  .hashtag { top: 945px; left: 230px; font-size: 27px; transform: rotate(-3deg); }
</style>
</head>
<body>
<div class="canvas">
  <section class="card">
    <svg class="jungle-collage" viewBox="0 0 703 997" aria-hidden="false">
      <rect width="703" height="997" fill="var(--indigo)"/>
      <g role="img" aria-label="Large blue palm leaf, upper left">
        <path d="M0 0 H170 L120 260 L0 300 Z" fill="var(--royal)"/>
      </g>
      <g role="img" aria-label="Teal leopard print patch">
        <path d="M80 0 H355 L340 240 L200 230 L110 150 Z" fill="var(--teal)"/>
        <path d="M330 0 H420 L400 260 L330 240 Z" fill="var(--sky)"/>
      </g>
      <g role="img" aria-label="Purple palm fronds, upper right">
        <path d="M300 0 H703 V420 L560 300 L420 230 L360 80 Z" fill="var(--purple)"/>
        <path d="M560 80 L703 40 V230 L620 300 Z" fill="var(--violet)"/>
      </g>
      <g role="img" aria-label="Magenta leaf background, left">
        <path d="M0 240 L200 300 L240 420 L120 520 L0 520 Z" fill="var(--magenta)"/>
      </g>
      <g role="img" aria-label="Green and blue macaw in flight">
        <path d="M0 190 Q120 170 250 240 Q280 320 230 380 Q140 330 90 260 Q40 240 0 250 Z" fill="var(--parrot)"/>
        <path d="M170 270 Q240 300 250 380 L180 390 Z" fill="var(--indigo)"/>
      </g>
      <g role="img" aria-label="Black and teal banded snake coiled on the left">
        <path d="M0 385 Q180 340 260 470 Q300 560 260 650 L220 690 Q200 560 150 500 Q80 440 0 460 Z" fill="var(--scale)" stroke="var(--magenta)" stroke-width="6"/>
        <path d="M0 520 Q90 520 120 600 L80 640 Q40 580 0 590 Z" fill="var(--teal)"/>
      </g>
      <g role="img" aria-label="Costumed partygoer in feathered headdress, shown in profile">
        <path d="M430 330 Q560 270 660 360 Q703 440 703 760 L560 760 Q440 700 420 560 Q400 430 430 330 Z" fill="var(--pale)" stroke="var(--lime)" stroke-width="8"/>
        <path d="M470 360 Q570 320 640 400 L600 470 Q530 420 470 430 Z" fill="var(--indigo)" opacity=".55"/>
      </g>
      <g role="img" aria-label="Dense blue and violet palm leaves along the bottom">
        <path d="M0 700 Q150 640 300 720 Q420 690 520 760 Q620 700 703 740 V997 H0 Z" fill="var(--purple)"/>
        <path d="M0 840 Q180 780 360 860 Q520 800 703 860 V997 H0 Z" fill="var(--royal)"/>
        <path d="M140 997 Q260 900 420 960 Q540 900 703 950 V997 Z" fill="var(--indigo)"/>
      </g>
    </svg>

    <h1 class="line title">Save The Date</h1>
    <p class="line place">Ibiza</p>
    <p class="line dates">4th to 7th June 2020</p>
    <p class="line hosts">Brenvik <small>b2b</small> Tarolo</p>
    <p class="line present">— Present —</p>
    <h2 class="line event">Dirty Thirty</h2>

    <p class="line label" style="top:442px">Official celebrations:</p>
    <p class="line item" style="top:474px">Boat cruise (Fri)</p>
    <p class="line item" style="top:507px">Birthday party (Sat)</p>

    <p class="line label" style="top:566px">Logistics:</p>
    <p class="line detail" style="top:593px">Flights available from FRA/DUS/TXL/MUC</p>

    <p class="line label" style="top:633px">Accommodation:</p>
    <p class="line detail" style="top:662px">Rooms available for all guests at hotel</p>
    <p class="line detail" style="top:692px">Casa Marisol (4*s) at special group rate</p>
    <p class="line detail" style="top:722px">(Promocode: „KRT30")</p>

    <p class="line theme" style="top:778px">Party theme: Ibiza Jungle</p>
    <p class="line detail" style="top:816px">No rules – strange, sultry, spooky, sexy or scant…</p>
    <p class="line detail" style="top:843px">You are expected to show a taste of radical</p>
    <p class="line detail" style="top:872px">self-expression, sensuality and extravagance</p>

    <p class="line rsvp">RSVP by 31 August 2019 to krt30@postwell.net</p>
    <p class="line hashtag">#KRT30</p>
  </section>
</div>
</body>
</html>
```